The Morrow Ledgers Website

I need a website to help promote the series of science fiction novels that I am in the process of writing.

I have some content and photos and am in the process of getting some new book cover artwork designed.

I have a current website/domain etc http://www.vantorpagehouse.co.nz but I need something a little more professional and eye catchig but I also want to be able to manage the content myself.

I can send e-versions of the two completed novels for context to any takers

```html
<!DOCTYPE html>
<html lang="en">
<head>
<meta charset="utf-8">
<title>Calder Wrenhall — The Morrow Ledgers</title>
<link rel="stylesheet" href="https://fonts.googleapis.com/css2?family=Tinos&family=PT+Sans:wght@400;700&family=Michroma&display=swap">
<style>
  :root {
    --page-bg: #e2ddd6;
    --header-bg: #00292a;
    --nav-bg: #5b3427;
    --nav-divider: #2e1710;
    --panel-bg: #ece8dc;
    --text: #111111;
    --accent-green: #1f7a12;
    --link-blue: #0000ee;
    --footer-bg: #121212;
    --footer-text: #a9a9a9;
    --sidebar-border: #9c9a92;
    --white: #ffffff;
  }
  * { box-sizing: border-box; margin: 0; padding: 0; }
  html, body { width: 1200px; height: 1000px; overflow: hidden; }
  body { background: var(--page-bg); font-family: "PT Sans", sans-serif; color: var(--text); position: relative; }

  .site-header {
    position: absolute; left: 51px; top: 0; width: 960px; height: 70px;
    background: var(--header-bg); border-radius: 0 0 5px 5px;
  }
  .site-title {
    position: absolute; left: 22px; top: 10px;
    font-family: "Tinos", serif; font-weight: 400; font-size: 44px; color: #f2f2ee;
  }

  .main-nav {
    position: absolute; left: 51px; top: 80px; width: 960px; height: 54px;
    background: var(--nav-bg); border-radius: 8px; display: flex;
  }
  .main-nav a {
    display: flex; align-items: center; justify-content: center;
    color: var(--white); text-decoration: none; font-size: 24px; font-weight: 700;
    border-right: 1px solid var(--nav-divider); height: 50px; margin-top: 3px;
  }

  .content-panel {
    position: absolute; left: 51px; top: 146px; width: 960px; height: 816px;
    background: var(--panel-bg); border-radius: 6px 6px 0 0;
  }

  .book-cover {
    position: absolute; left: 23px; top: 12px; width: 252px; height: 377px;
    background: linear-gradient(180deg, #e2973f 0%, #e0602a 30%, #f23a14 55%, #d9351a 80%, #c9421e 100%);
  }
  .availability { position: absolute; left: 27px; top: 393px; display: flex; gap: 8px; }
  .availability .label { color: var(--accent-green); font-size: 17px; font-weight: 700; }
  .availability ul { list-style: none; font-size: 14px; line-height: 18px; padding-top: 2px; }

  .series-title {
    position: absolute; left: 326px; top: 12px; width: 320px;
    font-family: "Michroma", sans-serif; font-size: 25px; line-height: 30px; font-weight: 400;
    letter-spacing: 0.5px;
  }
  .intro-heading { position: absolute; left: 328px; top: 88px; font-size: 20px; line-height: 23px; font-weight: 400; }
  .intro-text {
    position: absolute; left: 328px; top: 150px; width: 372px;
    font-size: 17px; line-height: 24px; text-indent: 32px;
  }
  .body-text {
    position: absolute; left: 27px; width: 650px; font-size: 17px; line-height: 21.5px; text-indent: 24px;
  }
  .body-text.first { top: 443px; }
  .body-text.second { top: 607px; text-indent: 45px; }

  .sidebar {
    position: absolute; left: 730px; top: 11px; width: 200px; height: 475px;
    border: 2px solid var(--sidebar-border); box-shadow: inset 0 0 3px rgba(0,0,0,0.15);
  }
  .author-photo {
    position: absolute; left: 23px; top: 13px; width: 150px; height: 145px;
    background: linear-gradient(135deg, #b3342a 0%, #7a2a25 40%, #4b3b36 70%, #8a8580 100%);
  }
  .author-blurb {
    position: absolute; left: 27px; top: 172px; width: 140px;
    font-size: 13px; line-height: 18px; word-break: break-all;
  }
  .author-blurb a { color: var(--link-blue); text-decoration: none; font-weight: 700; }
  .sidebar-links { position: absolute; left: 21px; top: 274px; list-style: none; }
  .sidebar-links li { height: 34px; }
  .sidebar-links a { color: var(--link-blue); text-decoration: none; font-size: 14px; font-weight: 700; }

  .site-footer {
    position: absolute; left: 51px; top: 962px; width: 960px; height: 38px;
    background: var(--footer-bg);
  }
  .footer-nav { position: absolute; left: 22px; top: 12px; font-size: 13px; color: var(--footer-text); }
  .footer-nav a { color: var(--footer-text); text-decoration: none; text-transform: uppercase; }
</style>
</head>
<body>
  <header class="site-header">
    <h1 class="site-title">Calder Wrenhall</h1>
  </header>

  <nav class="main-nav">
    <a href="#" style="width:116px">Home</a>
    <a href="#" style="width:122px">Book</a>
    <a href="#" style="width:145px">Reviews</a>
    <a href="#" style="width:123px">Author</a>
    <a href="#" style="width:124px">Blog</a>
    <a href="#" style="width:147px">Contact</a>
  </nav>

  <main class="content-panel">
    <div class="book-cover" role="img" aria-label="Book cover artwork for the second novel in The Morrow Ledgers"></div>
    <div class="availability">
      <span class="label">Avaliable:</span>
      <ul><li>kindle version</li><li>Hard Copy</li></ul>
    </div>

    <h2 class="series-title">The Morrow Ledgers</h2>
    <h3 class="intro-heading">Your Introductry content<br>goes here:</h3>
    <p class="intro-text">Lorem ipsum dolor sit amet, consectetuer adipiscing elit, sed diam nonummy nibh euismod tincidunt ut laoreet dolore magna aliquam erat volutpat. Ut wisi enim ad minim veniam, quis nostrud exerci tation ullamcorper suscipit lobortis nisl ut aliquip ex ea commodo consequat. Duis autem vel eum iriure dolor in hendrerit in vulputate velit esse molestie consequat, vel illum dolor sjklsjkljskflj;lkjfl; skfjlsadkjflkasjdfajsdf;ajsdf;lkadsjalksdfjjfsdl jsfljlksdjflaksjfldkajslfdkajsfaakslfsdjfljafslaf skdjflafs;lkdjaklsdfjalksfj;alksjdf;klsdfj</p>

    <p class="body-text first">Lorem ipsum dolor sit amet, consectetuer adipiscing elit, sed diam nonummy nibh euismod tincidunt ut laoreet dolore magna aliquam erat volutpat. Ut wisi enim ad minim veniam, quis nostrud exerci tation ullamcorper suscipit lobortis nisl ut aliquip ex ea commodo consequat. Duis autem vel eum iriure dolor in hendrerit in vulputate velit esse molestie consequat, vel illum dolore eu feugiat nulla facilisis at vero eros et accumsan et iusto odio dignissim qui blandit praesent luptatum zzril delenit augue duis dolore te feugait nulla facilisi.</p>
    <p class="body-text second">Lorem ipsum dolor sit amet, consectetuer adipiscing elit, sed diam nonummy nibh euismod tincidunt ut laoreet dolore magna aliquam erat volutpat. Ut wisi enim ad minim veniam, quis nostrud exerci tation ullamcorper suscipit lobortis nisl ut aliquip ex ea commodo consequat. Duis autem vel eum iriure dolor in hendrerit in vulputate velit esse molestie consequat, vel illum dolore eu feugiat nulla facilisis at vero eros et accumsan et iusto odio dignissim qui blandit praesent luptatum zzril delenit augue duis dolore te feugait nulla facilisi.</p>

    <aside class="sidebar">
      <div class="author-photo" role="img" aria-label="Portrait photograph of the author"></div>
      <p class="author-blurb">jslfdjfas;lkafsjfas dfsjlafjk; ljlkjlkjljljljjl kljljjljljlj kljlkjjlkjlji ljkj <a href="#">read more..</a></p>
      <ul class="sidebar-links">
        <li><a href="#">more LInks goes here</a></li>
        <li><a href="#">more LInks goes here</a></li>
        <li><a href="#">more LInks goes here</a></li>
        <li><a href="#">more LInks goes here</a></li>
      </ul>
    </aside>
  </main>

  <footer class="site-footer">
    <nav class="footer-nav">
      <a href="#">Home</a> | <a href="#">Books</a> | <a href="#">Reviews</a> | <a href="#">Author</a> | <a href="#">Blog</a> | <a href="#">Contact</a>
    </nav>
  </footer>
</body>
</html>
```